Professional Report Cover

We need a cover for CFO report (the document is about 20 pages, in case you decide to provide 3D mockup). The design must be professional. The main color has to be #299FC0, which can be incorporated with white, #375172, and #E3E7EE. See attached for content and logo.

```html
<!DOCTYPE html>
<html lang="en">
<head>
<meta charset="utf-8">
<title>The CFO Insight – Report Cover</title>
<link rel="stylesheet" href="https://fonts.googleapis.com/css2?family=Cinzel:wght@400&family=Open+Sans:wght@600;700&family=Saira+Extra+Condensed:wght@500;600&display=swap">
<style>
  :root {
    --teal: #299FC0;
    --teal-soft: #3EA9C8;
    --navy: #375172;
    --navy-deep: #1F3A63;
    --mist: #E3E7EE;
    --mist-deep: #CBD3E0;
    --slate: #9FABBA;
    --white: #FFFFFF;
    --ink: #111418;
    --stage: #F2F3F5;
  }
  * { box-sizing: border-box; margin: 0; padding: 0; }
  html, body {
    width: 1200px;
    height: 1107px;
    overflow: hidden;
    background: var(--stage);
  }
  .cover {
    position: absolute;
    left: 225px;
    top: 30px;
    width: 750px;
    height: 1047px;
    background: var(--white);
    overflow: hidden;
    box-shadow: 0 6px 24px rgba(31, 58, 99, 0.18);
  }
  .cover-art {
    position: absolute;
    inset: 0;
    width: 100%;
    height: 100%;
  }
  .brand {
    position: absolute;
    left: 58px;
    top: 120px;
    width: 215px;
    padding-left: 14px;
    border-left: 2px solid var(--ink);
  }
  .brand-name {
    display: flex;
    align-items: center;
    gap: 9px;
    font-family: "Open Sans", sans-serif;
    font-weight: 700;
    font-size: 17px;
    line-height: 1.2;
    color: var(--ink);
  }
  .brand-mark {
    flex: 0 0 12px;
    width: 12px;
    height: 12px;
    background: var(--ink);
  }
  .brand-tagline {
    margin-top: 8px;
    font-family: "Open Sans", sans-serif;
    font-weight: 600;
    font-size: 9px;
    letter-spacing: 1.6px;
    text-transform: uppercase;
    color: #555b66;
  }
  .title {
    position: absolute;
    left: 375px;
    top: 175px;
    width: 340px;
    height: 400px;
  }
  .title-art {
    width: 100%;
    height: 100%;
    overflow: visible;
  }
  .title-the,
  .title-sub {
    font-family: "Cinzel", serif;
    fill: var(--white);
  }
  .title-the { font-size: 40px; }
  .title-sub { font-size: 56px; }
  .title-main {
    font-family: "Saira Extra Condensed", sans-serif;
    font-weight: 600;
    font-size: 250px;
    fill: var(--white);
  }
  .includes {
    position: absolute;
    left: 60px;
    top: 770px;
    width: 640px;
  }
  .includes-heading {
    font-family: "Saira Extra Condensed", sans-serif;
    font-weight: 500;
    font-size: 38px;
    letter-spacing: 1px;
    color: var(--navy);
    margin-bottom: 14px;
  }
  .includes-list { list-style: none; }
  .includes-item {
    display: flex;
    gap: 16px;
    align-items: flex-start;
    margin-bottom: 14px;
    font-family: "Open Sans", sans-serif;
    font-weight: 600;
    font-size: 19px;
    line-height: 1.3;
    color: var(--ink);
  }
  .tick {
    flex: 0 0 20px;
    width: 20px;
    height: 22px;
    margin-top: 2px;
  }
</style>
</head>
<body>
  <main class="cover">
    <svg class="cover-art" viewBox="0 0 750 1047" aria-hidden="true">
      <rect x="40" y="0" width="70" height="680" fill="var(--mist)"/>
      <rect x="160" y="0" width="150" height="560" fill="var(--mist)"/>
      <rect x="245" y="0" width="40" height="600" fill="var(--mist-deep)" opacity="0.7"/>
      <rect x="300" y="600" width="40" height="447" fill="var(--mist)" opacity="0.6"/>
      <rect x="420" y="700" width="70" height="347" fill="var(--mist)" opacity="0.45"/>
      <rect x="560" y="760" width="90" height="287" fill="var(--mist)" opacity="0.35"/>
      <rect x="292" y="30" width="6" height="200" fill="var(--teal)"/>
      <rect x="118" y="300" width="6" height="170" fill="var(--teal)"/>
      <polygon points="320,0 750,0 750,470 470,640 320,560" fill="var(--navy)"/>
      <polygon points="560,0 750,0 750,470 620,550" fill="var(--navy-deep)" opacity="0.35"/>
      <polygon points="175,300 330,240 330,560 470,640 420,690 175,600" fill="var(--teal-soft)"/>
      <polygon points="250,290 330,260 330,560 470,640 440,660 250,590" fill="var(--teal)" opacity="0.75"/>
      <polygon points="750,470 750,780 400,680 470,640" fill="var(--slate)"/>
    </svg>

    <div class="brand">
      <div class="brand-name"><span class="brand-mark"></span><span>Northvale<br>Document Services</span></div>
      <div class="brand-tagline">A Meridian Group Company</div>
    </div>

    <h1 class="title" aria-label="The CFO Insight">
      <svg class="title-art" viewBox="0 0 340 400">
        <text class="title-the" x="170" y="48" text-anchor="middle" textLength="110" lengthAdjust="spacingAndGlyphs">THE</text>
        <text class="title-main" x="20" y="300" textLength="300" lengthAdjust="spacingAndGlyphs">CFO</text>
        <text class="title-sub" x="20" y="372" textLength="300" lengthAdjust="spacingAndGlyphs">INSIGHT</text>
      </svg>
    </h1>

    <section class="includes">
      <h2 class="includes-heading">INCLUDES:</h2>
      <ul class="includes-list">
        <li class="includes-item">
          <svg class="tick" viewBox="0 0 20 22"><path d="M2 16 L8 20 L12 2" fill="none" stroke="var(--navy)" stroke-width="4"/></svg>
          <span>Insights into external, enterprise and departmental challenges</span>
        </li>
        <li class="includes-item">
          <svg class="tick" viewBox="0 0 20 22"><path d="M2 16 L8 20 L12 2" fill="none" stroke="var(--navy)" stroke-width="4"/></svg>
          <span>Best practices and strategies to solve these challenges, with a focus on innovation, securing competitive advantages and opportunities for growth</span>
        </li>
        <li class="includes-item">
          <svg class="tick" viewBox="0 0 20 22"><path d="M2 16 L8 20 L12 2" fill="none" stroke="var(--navy)" stroke-width="4"/></svg>
          <span>Finance industry trends in the 2020s</span>
        </li>
        <li class="includes-item">
          <svg class="tick" viewBox="0 0 20 22"><path d="M2 16 L8 20 L12 2" fill="none" stroke="var(--navy)" stroke-width="4"/></svg>
          <span>The leading role of CFOs in business transformation</span>
        </li>
      </ul>
    </section>
  </main>
</body>
</html>
```